Townhome Multi-Family Property Exterior Sign

Hello. We are looking for a new design for our exterior pylon for for a multi-family housing property in Texas. The design will need to go on a new sign panel to replace the existing (see photo of existing). We are looking to see both modern and contemporary designs. Included the sign should be the name, Loma Brisa Townhomes and the web address www.lomabrisatownhomes.example.

Attached here is a PDF file of the proposed new sign shape. We are open to other shape ideas as well if your design would better suit a more rectangular shape.

Industry/Entity Type

Property

Font styles to use
Serif
Sans Serif

Colors
9bcb3c

Requirements
Must have
• Name of building: Loma Brisa Townhomes
• Website: www.lomabrisatownhomes.example
Nice to have
• Address: 420-530 Halvorsen Lane (only if it fits nicely)

```html
<!DOCTYPE html>
<html lang="en">
<head>
<meta charset="utf-8">
<title>Loma Brisa Townhomes – Exterior Sign</title>
<link rel="stylesheet" href="https://fonts.googleapis.com/css2?family=Montserrat:wght@700;800;900&display=swap">
<style>
  :root {
    --bg: #e4e4e4;
    --panel: #ffffff;
    --brand-green: #2fae4a;
    --ink: #333438;
    --band-light: #39b54a;
    --band-dark: #1e8a3c;
    --band-highlight: #2fd160;
    --wave-line: #2a2b2f;
    --mint: #b8f5cc;
    --white: #ffffff;
  }
  html, body {
    margin: 0;
    padding: 0;
    width: 1200px;
    height: 1000px;
    overflow: hidden;
    background: var(--bg);
  }
  .canvas {
    position: relative;
    width: 1200px;
    height: 1000px;
  }
  .sign-panel {
    position: absolute;
    left: 87px;
    top: 248px;
    width: 1026px;
    height: 487px;
    display: block;
  }
  .sign-text {
    font-family: "Montserrat", sans-serif;
  }
  .property-name {
    font-weight: 800;
    font-size: 134px;
    fill: var(--brand-green);
  }
  .property-type {
    font-weight: 800;
    font-size: 134px;
    fill: var(--ink);
  }
  .web-address {
    font-weight: 800;
    font-size: 38px;
    fill: var(--white);
  }
  .web-address .domain { fill: var(--mint); }
  .street-address {
    font-weight: 800;
    font-size: 29px;
    fill: var(--white);
  }
  .globe-icon { fill: none; stroke: var(--white); stroke-width: 2.6; }
</style>
</head>
<body>
<main class="canvas">
  <svg class="sign-panel" viewBox="0 0 1026 487" xmlns="http://www.w3.org/2000/svg" aria-label="Loma Brisa Townhomes sign">
    <defs>
      <linearGradient id="band-fill" x1="0" y1="0" x2="1" y2="0">
        <stop offset="0" stop-color="var(--band-dark)"/>
        <stop offset="0.45" stop-color="var(--band-light)"/>
        <stop offset="1" stop-color="var(--band-dark)"/>
      </linearGradient>
    </defs>

    <rect class="panel-face" width="1026" height="487" fill="var(--panel)"/>

    <!-- wave band -->
    <path class="wave-line" d="M0 300 C 200 352, 450 322, 620 278 C 760 242, 900 255, 1026 312 L1026 322 C 900 266, 760 254, 620 290 C 450 334, 200 364, 0 312 Z" fill="var(--wave-line)"/>
    <path class="wave-highlight" d="M0 312 C 200 364, 450 334, 620 290 C 760 254, 900 266, 1026 322 L1026 487 L0 487 Z" fill="var(--band-highlight)"/>
    <path class="wave-band" d="M0 328 C 200 376, 450 350, 620 306 C 760 272, 900 282, 1026 336 L1026 487 L0 487 Z" fill="url(#band-fill)"/>

    <!-- name -->
    <text class="sign-text property-name" x="513" y="137" text-anchor="middle" textLength="878" lengthAdjust="spacingAndGlyphs">LOMA BRISA</text>
    <text class="sign-text property-type" x="513" y="244" text-anchor="middle" textLength="878" lengthAdjust="spacingAndGlyphs">TOWNHOMES</text>

    <!-- globe icon -->
    <g class="globe-icon" transform="translate(100 413)">
      <circle r="16"/>
      <ellipse rx="7" ry="16"/>
      <line x1="-16" y1="0" x2="16" y2="0"/>
      <line x1="-13" y1="-8" x2="13" y2="-8"/>
      <line x1="-13" y1="8" x2="13" y2="8"/>
      <line x1="0" y1="-16" x2="0" y2="16"/>
    </g>

    <text class="sign-text web-address" x="128" y="427" textLength="812" lengthAdjust="spacingAndGlyphs">WWW.<tspan class="domain">LOMABRISATOWNHOMES</tspan>.EXAMPLE</text>
    <text class="sign-text street-address" x="513" y="465" text-anchor="middle">420-530 HALVORSEN LANE</text>
  </svg>
</main>
</body>
</html>
```